Children's Educational Software - Login Screens

We need graphics for some basic login pages. The main requirements are a background image, buttons and background overlay (box for login fields and app icons). Must utilize responsive design for various resolutions and devices. The mock-up file provides an example of the direction we are wanting to go. The app page will require a version of the background that extends down using a solid colour. One idea would be to add some flowers, bees, etc. to help add some life to the bottom half. I like the idea of clouds and grass, but am open to anything.

Target Market(s)

Elementary teachers and young children

Coding

Coded - Design and coding required

Number of Pages Required

2 page

Font styles to use
Sans Serif

Requirements
Must have
• Responsive design for various resolutions and devices
Nice to have
• clouds, grass, new app icons if current icons don't fit with new design

```html
<!DOCTYPE html>
<html lang="en">
<head>
<meta charset="UTF-8">
<title>Teacher Login – BrightSteps</title>
<link href="https://fonts.googleapis.com/css2?family=Roboto:wght@400;500;700&display=swap" rel="stylesheet">
<style>
:root{
  --sky-top:#a9d4f3;
  --sky-low:#d6eef7;
  --grass-light:#a6d13a;
  --grass-deep:#8cc02a;
  --brand:#2e4a96;
  --panel-frame:rgba(222,240,196,.8);
  --panel:#2f4585;
  --white:#ffffff;
  --field:#f4f4f4;
  --teal:#12c2ae;
  --teal-deep:#0aa795;
  --red:#d11e0c;
  --red-deep:#a81005;
  --footer:#1f3175;
}
*{box-sizing:border-box;margin:0;padding:0}
html,body{width:1200px;height:813px;overflow:hidden}
body{font-family:"Roboto",Arial,sans-serif;position:relative;background:var(--sky-top)}
.scene{position:absolute;inset:0;
  background:linear-gradient(180deg,var(--sky-top) 0%,var(--sky-low) 55%,var(--grass-light) 68%,var(--grass-deep) 100%)}
.brand{position:absolute;left:38px;top:56px;display:flex;align-items:center;gap:18px;height:72px}
.brand__mark{width:72px;height:72px;background:var(--brand);border-radius:6px}
.brand__name{font-size:46px;font-weight:500;color:var(--brand);letter-spacing:-.5px;line-height:1}
.login-frame{position:absolute;left:318px;top:194px;width:583px;height:478px;border-radius:10px;background:var(--panel-frame)}
.login-card{position:absolute;left:330px;top:206px;width:559px;height:453px;border-radius:10px;background:var(--panel);color:var(--white)}
.login-card__title{position:absolute;left:0;right:0;top:50px;display:flex;justify-content:center;align-items:center;gap:14px;font-size:37px;font-weight:500;line-height:44px}
.login-card__title svg{width:42px;height:44px}
.login-card__lead{position:absolute;left:0;right:0;top:107px;text-align:center;font-size:14px;font-weight:500}
.field{position:absolute;left:0;display:flex;align-items:center}
.field label{width:240px;text-align:right;padding-right:12px;font-size:14px;font-weight:500}
.field input{width:207px;height:43px;border:1px solid #d8d8d8;border-radius:3px;
  background:linear-gradient(180deg,#ffffff 0%,var(--field) 50%,#ffffff 100%);box-shadow:inset 0 2px 4px rgba(0,0,0,.15)}
.field--user{top:161px}
.field--pass{top:225px}
.btn{position:absolute;height:40px;width:154px;border-radius:8px;border:2px solid rgba(255,255,255,.8);
  color:var(--white);font:500 14px "Roboto",Arial,sans-serif;display:flex;align-items:center;justify-content:center}
.btn--back{left:125px;top:295px;background:linear-gradient(180deg,var(--teal),var(--teal-deep))}
.btn--login{left:295px;top:295px;background:linear-gradient(180deg,var(--red),var(--red-deep))}
.btn--legacy{left:389px;top:375px;background:linear-gradient(180deg,var(--red),var(--red-deep))}
.login-card__note{position:absolute;left:38px;top:386px;font-size:14px;font-weight:500}
.footer{position:absolute;left:0;right:0;bottom:0;height:47px;background:var(--footer);color:var(--white);
  font-size:13px;font-weight:500;display:flex;align-items:center;justify-content:space-between;padding:0 62px 0 66px}
.footer__contact span{margin:0 13px}
</style>
</head>
<body>
<div class="scene" role="img" aria-label="Illustrated landscape: sunny blue sky, clouds and green grass hills with trees, and a cartoon teacher holding books at the lower left"></div>

<header class="brand">
  <span class="brand__mark"></span>
  <span class="brand__name">BrightSteps</span>
</header>

<div class="login-frame"></div>
<main class="login-card">
  <h1 class="login-card__title">
    <svg viewBox="0 0 42 44" aria-hidden="true">
      <circle cx="19" cy="11" r="8" fill="none" stroke="#fff" stroke-width="3"/>
      <path d="M3 42c0-10 7-17 16-17s16 7 16 17z" fill="#fff"/>
      <circle cx="34" cy="36" r="7" fill="#fff" stroke="#2f4585" stroke-width="2"/>
      <rect x="31" y="35" width="6" height="5" fill="#2f4585"/>
      <path d="M32 35v-2a2 2 0 0 1 4 0v2" fill="none" stroke="#2f4585" stroke-width="1.4"/>
    </svg>
    Teacher Login
  </h1>
  <p class="login-card__lead">Type Your Username and password to access the Teacher Dashboard</p>
  <div class="field field--user"><label for="user">Username:</label><input id="user" type="text"></div>
  <div class="field field--pass"><label for="pass">Password:</label><input id="pass" type="password"></div>
  <button class="btn btn--back">Back</button>
  <button class="btn btn--login">Login</button>
  <p class="login-card__note">Note : Login Previous Version of the Dashboard here</p>
  <button class="btn btn--legacy">Legacy Login</button>
</main>

<footer class="footer">
  <p>Copyright © 2019 BrightSteps Learning. All Right Reserved</p>
  <p class="footer__contact">1-800-555-0142<span>|</span>hello@brightsteps.example</p>
</footer>
</body>
</html>
```